Aircraft maintenance buisness card

I am an aircraft mechanic looking for a personal buisness card . I would like my name and a title of Aircraft Maintenance Manager . I would like a suttle picture of an aircraft and helicopter .

elegant and professional wtih my contact .

My name should be on the car and Aircraft Maintenance Manager under with my contact infor below .

i have attached some pictures but i am open to other pics and ideas . I would like a airliner or private jet and a helicopter in the picture . The Images should be suttle and not the main idea . I also uploaded a picture of a jet engine which is cool . Be creative and i will work with you to finalize something .
Updates

Project Deadline Extended
Reason: Looking for more variations . Very good so far but looiking for a bit more styles and i uploaded my logo that i purchased . Please use my logo and be creative with it . I like some variations of black card with maybe some pictures that i uploaded but i am open to ideas . Be creative and i will work with you .

Project Deadline Extended
Reason: Looking for more designs and variations . Not yet satisfied with the designs i have gotten .

Industry/Entity Type

Aviation

Contact Information for Business Card

Aircraft Maintenance Manager

Font styles to use
Serif

Colors

Designer to choose colors to be used in the design.

Requirements
Must have
• An aviation related Logo if possible incorporated in the card possibly
• My name
• Tiberio Malvade Furtunato
• 482 Pellow St.
• Kearny , NJ
• 08519
• Email: Lwskyfixtech@mailvora.com
Nice to have
• Suttle Backround of a Private Jet or Airliner and a Helicopter .

```html
<!DOCTYPE html>
<html lang="en">
<head>
<meta charset="utf-8">
<title>Corvane Aviation – Business Card</title>
<link href="https://fonts.googleapis.com/css2?family=Montserrat:ital,wght@0,400;0,500;0,700;1,400&display=swap" rel="stylesheet">
<style>
  :root {
    --stage: #d4d4d4;
    --card-black: #000000;
    --card-white: #ffffff;
    --sky-blue: #1aa3e8;
    --royal-blue: #1a4fb0;
    --deep-blue: #0d46a8;
    --rule-blue: #1d4fb8;
    --text-light: #ffffff;
    --photo-jet-a: #8fa9bd;
    --photo-jet-b: #5f7d8a;
    --photo-heli-a: #7b7f7c;
    --photo-heli-b: #4e5a63;
  }
  * { margin: 0; padding: 0; box-sizing: border-box; }
  html, body { width: 1200px; height: 798px; overflow: hidden; }
  body {
    background: var(--stage);
    position: relative;
    font-family: "Montserrat", sans-serif;
  }
  .card {
    position: absolute;
    width: 520px;
    height: 297px;
    background: var(--card-white);
    overflow: hidden;
  }
  .card-front { left: 396px; top: 85px; }
  .card-back  { left: 396px; top: 446px; }
  .card-art { position: absolute; inset: 0; width: 100%; height: 100%; }

  .brand {
    position: absolute;
    display: flex;
    align-items: center;
    gap: 8px;
    color: var(--royal-blue);
    font-weight: 700;
    white-space: nowrap;
  }
  .brand-mark {
    display: block;
    background: var(--royal-blue);
    border-radius: 6px;
  }
  .brand-front { left: 170px; top: 125px; font-size: 18px; }
  .brand-front .brand-mark { width: 42px; height: 42px; }
  .brand-back { right: 16px; top: 32px; font-size: 14px; gap: 6px; }
  .brand-back .brand-mark { width: 28px; height: 28px; border-radius: 4px; }

  .holder {
    position: absolute;
    left: 21px;
    top: 117px;
    padding-left: 9px;
    border-left: 2px solid var(--rule-blue);
  }
  .holder-name {
    color: var(--sky-blue);
    font-weight: 700;
    font-size: 13.5px;
    letter-spacing: 0.1px;
    line-height: 16px;
    text-transform: uppercase;
  }
  .holder-title {
    color: var(--text-light);
    font-style: italic;
    font-size: 8.6px;
    line-height: 11px;
    text-transform: uppercase;
  }
  .contact {
    position: absolute;
    left: 0;
    display: flex;
    align-items: center;
    color: var(--text-light);
    font-size: 10.4px;
  }
  .contact svg { flex: none; }
  .contact-email { top: 169px; left: 19px; gap: 10px; }
  .contact-address { top: 201px; left: 24px; gap: 12px; }
</style>
</head>
<body>

  <section class="card card-front" aria-label="Business card front">
    <svg class="card-art" viewBox="0 0 520 297" aria-hidden="true">
      <polygon points="0,0 166,0 14,297 0,297" fill="var(--card-black)"/>
      <line x1="166" y1="0" x2="12" y2="297" stroke="var(--deep-blue)" stroke-width="1.5"/>
      <polygon points="97,165 106,160 18,297 9,297" fill="var(--deep-blue)"/>
      <polygon points="90,176 96,172 10,297 4,297" fill="var(--sky-blue)"/>
    </svg>
    <div class="brand brand-front">
      <span class="brand-mark"></span>
      <span class="brand-name">Corvane Aviation</span>
    </div>
  </section>

  <section class="card card-back" aria-label="Business card back">
    <svg class="card-art" viewBox="0 0 520 297">
      <defs>
        <linearGradient id="jetTone" x1="0" y1="0" x2="0" y2="1">
          <stop offset="0" stop-color="var(--photo-jet-a)"/>
          <stop offset="1" stop-color="var(--photo-jet-b)"/>
        </linearGradient>
        <linearGradient id="heliTone" x1="0" y1="0" x2="1" y2="1">
          <stop offset="0" stop-color="var(--photo-heli-a)"/>
          <stop offset="1" stop-color="var(--photo-heli-b)"/>
        </linearGradient>
      </defs>
      <polygon points="0,0 182,0 432,297 0,297" fill="var(--card-black)"/>
      <line x1="182" y1="0" x2="432" y2="297" stroke="var(--rule-blue)" stroke-width="1.5"/>
      <polygon points="182,0 206,0 293,110 269,110" fill="var(--sky-blue)"/>

      <line x1="0" y1="161" x2="318" y2="161" stroke="var(--rule-blue)" stroke-width="1"/>
      <line x1="0" y1="193" x2="345" y2="193" stroke="var(--rule-blue)" stroke-width="1"/>
      <line x1="0" y1="223" x2="370" y2="223" stroke="var(--rule-blue)" stroke-width="1"/>

      <polygon points="310,113 322,113 390,193 378,193" fill="var(--card-white)"/>
      <polygon points="322,113 338,113 405,193 390,193" fill="var(--royal-blue)"/>
      <polygon points="338,113 350,113 418,193 405,193" fill="var(--sky-blue)"/>
      <polygon points="350,113 522,113 522,193 418,193" fill="url(#jetTone)" role="img" aria-label="Photo of a wide-body airliner flying above a coastline"/>

      <polygon points="387,206 400,206 466,285 453,285" fill="var(--sky-blue)"/>
      <polygon points="400,206 413,206 479,285 466,285" fill="var(--royal-blue)"/>
      <polygon points="413,206 522,206 522,285 479,285" fill="url(#heliTone)" role="img" aria-label="Photo of a helicopter flying past a rocky cliff"/>
    </svg>

    <div class="brand brand-back">
      <span class="brand-mark"></span>
      <span class="brand-name">Corvane Aviation</span>
    </div>

    <div class="holder">
      <p class="holder-name">Tiberio Malvade Furtunato</p>
      <p class="holder-title">Aircraft Maintenance Manager</p>
    </div>

    <p class="contact contact-email">
      <svg width="20" height="14" viewBox="0 0 20 14" aria-hidden="true">
        <rect x="0.75" y="0.75" width="18.5" height="12.5" fill="none" stroke="#fff" stroke-width="1.2"/>
        <polyline points="1,1 10,8 19,1" fill="none" stroke="#fff" stroke-width="1.2"/>
        <line x1="1" y1="13" x2="8" y2="6.5" stroke="#fff" stroke-width="1.2"/>
        <line x1="19" y1="13" x2="12" y2="6.5" stroke="#fff" stroke-width="1.2"/>
      </svg>
      <span>lwskyfixtech@mailvora.com</span>
    </p>

    <p class="contact contact-address">
      <svg width="11" height="15" viewBox="0 0 11 15" aria-hidden="true">
        <path d="M5.5 0C2.5 0 0 2.4 0 5.4 0 9.4 5.5 15 5.5 15S11 9.4 11 5.4C11 2.4 8.5 0 5.5 0Z" fill="#fff"/>
        <circle cx="5.5" cy="5.4" r="2.1" fill="var(--card-black)"/>
      </svg>
      <span>482 Pellow St., Brenmoor, PA 08519</span>
    </p>
  </section>

</body>
</html>
```